120 years jubilee KORVIL und DASCHE

We are celebrating very proud our 120 years in 5 generations
see our briefing
the invitations card should look elegant, modern, colourful as we are
our motto: mirrorpicture

```html
<!DOCTYPE html>
<html lang="en">
<head>
<meta charset="utf-8">
<title>Mirror Picture – 120 Years Korvil &amp; Dasche</title>
<link href="https://fonts.googleapis.com/css2?family=Great+Vibes&family=Josefin+Sans:ital,wght@0,400;0,600;0,700;1,700&display=swap" rel="stylesheet">
<style>
  :root {
    --wine: #5b1a28;
    --wine-deep: #4e1622;
    --rust: #e04b24;
    --rust-soft: #c9552f;
    --line: #8a3b2c;
    --paper: #ffffff;
    --lilac: #d6d0e6;
    --ink-light: #ffffff;
  }
  * { margin: 0; padding: 0; box-sizing: border-box; }
  html, body { width: 920px; height: 1200px; overflow: hidden; background: var(--paper); }
  .invitation {
    position: relative; width: 920px; height: 1200px; background: var(--paper);
    font-family: "Josefin Sans", sans-serif; color: var(--wine); overflow: hidden;
  }
  .frame { position: absolute; background: var(--line); }
  .frame--top { left: 215px; top: 38px; width: 656px; height: 1px; }
  .frame--right { left: 870px; top: 38px; width: 1px; height: 661px; }
  .frame--left { left: 49px; top: 166px; width: 1px; height: 533px; }

  .leaf-spray {
    position: absolute; left: 0; top: 0; width: 240px; height: 150px;
    background: radial-gradient(ellipse at 40% 40%, rgba(201,85,47,.28), rgba(91,26,40,.06) 70%, transparent 75%);
  }
  .flower-spray {
    position: absolute; left: 508px; top: 301px; width: 212px; height: 218px;
    background: radial-gradient(ellipse at 55% 45%, rgba(224,75,36,.28), rgba(91,26,40,.08) 65%, transparent 72%);
  }

  .brand-name {
    position: absolute; left: 0; width: 920px; top: 60px; text-align: center;
    font-size: 30px; font-weight: 400; color: #1d1d1d; letter-spacing: -.5px;
  }
  .jubilee-emblem {
    position: absolute; left: 315px; top: 106px; width: 288px; height: 129px;
    background: linear-gradient(90deg, var(--lilac) 0%, var(--wine) 40%, var(--rust) 100%);
    border-radius: 4px;
  }

  .motto { position: absolute; font-family: "Great Vibes", cursive; line-height: 1; }
  .motto--mirror { left: 200px; top: 305px; font-size: 128px; color: var(--wine); }
  .motto--picture { left: 362px; top: 410px; font-size: 118px; color: var(--rust); }

  .tagline {
    position: absolute; left: 0; width: 880px; top: 550px; text-align: center;
    font-size: 29px; font-weight: 700; font-style: italic; letter-spacing: .8px; color: var(--wine);
  }
  .since-pill {
    position: absolute; left: 275px; top: 588px; width: 326px; height: 60px;
    border: 2px solid var(--rust); border-radius: 30px;
    display: flex; align-items: center; justify-content: center; text-align: center;
    font-size: 21px; line-height: 24px; letter-spacing: .8px; color: var(--wine); padding-top: 4px;
  }

  .event-band {
    position: absolute; left: 0; top: 699px; width: 920px; height: 501px; color: var(--ink-light);
    background: linear-gradient(90deg, var(--rust) 0%, #a73328 12%, var(--wine-deep) 28%, #7a2329 50%, #b83a28 70%, var(--rust) 84%, #c4402a 94%, #a8352b 100%);
  }
  .event-date {
    position: absolute; top: 32px; left: 0; width: 920px; height: 60px;
    font-size: 40px; font-weight: 600; letter-spacing: 1px;
  }
  .event-date span { position: absolute; top: 12px; }
  .event-date .day { left: 228px; }
  .event-date .month { left: 305px; }
  .event-date .year { left: 595px; }
  .event-date .divider { position: absolute; top: 0; width: 2px; height: 58px; background: var(--ink-light); }

  .rule { position: absolute; left: 243px; width: 434px; height: 12px; }
  .rule--upper { top: 106px; }
  .rule--lower { top: 388px; }

  .programme { position: absolute; left: 0; width: 920px; text-align: center; }
  .programme__label {
    display: inline-block; background: var(--wine); border-radius: 15px; padding: 6px 18px 3px;
    font-size: 19px; font-weight: 700; font-style: italic; letter-spacing: 1px;
  }
  .programme__items { margin-top: 6px; font-size: 18px; line-height: 18px; letter-spacing: 1px; }
  .programme--designers { top: 127px; }
  .programme--liveshows { top: 210px; }
  .programme--showroom { top: 327px; }

  .venue {
    position: absolute; left: 0; width: 920px; top: 430px; text-align: center;
    font-size: 16.5px; line-height: 20px; letter-spacing: .5px;
  }
</style>
</head>
<body>
<main class="invitation">
  <div class="leaf-spray" role="img" aria-label="Line-drawn autumn leaf spray in copper tones"></div>
  <div class="frame frame--top"></div>
  <div class="frame frame--right"></div>
  <div class="frame frame--left"></div>

  <div class="brand-name">Korvil &amp; Dasche</div>
  <div class="jubilee-emblem" role="img" aria-label="120 years jubilee emblem"></div>

  <div class="flower-spray" role="img" aria-label="Line-drawn flower and leaf sprig in rust and wine"></div>
  <h1 class="motto motto--mirror">Mirror</h1>
  <div class="motto motto--picture">Picture</div>

  <h2 class="tagline">THE ART OF RECOGNITION</h2>
  <div class="since-pill">proud of our 5 generations<br>in 120 years -since 1903</div>

  <section class="event-band">
    <div class="event-date">
      <span class="day">15</span>
      <i class="divider" style="left:262px"></i>
      <span class="month">SEPTEMBER</span>
      <i class="divider" style="left:574px"></i>
      <span class="year">2023</span>
    </div>

    <svg class="rule rule--upper" viewBox="0 0 434 12" aria-hidden="true">
      <line x1="6" y1="6" x2="428" y2="6" stroke="#e04b24" stroke-width="1.4"/>
      <path d="M2 0 L6 6 L2 12 Z M432 0 L428 6 L432 12 Z" fill="#e04b24"/>
      <circle cx="217" cy="6" r="1.6" fill="#e04b24"/>
    </svg>

    <div class="programme programme--designers">
      <span class="programme__label">DESIGNERS</span>
      <p class="programme__items">Lena Morvay "today is euphoria"<br>Otto Brenk "reflection of art"</p>
    </div>

    <div class="programme programme--liveshows">
      <span class="programme__label">LIVESHOWS</span>
      <p class="programme__items">How the Viennese weave is created<br>How the Halden Lounge Chair is created<br>Building a Modul shelf yourself<br>Experience 3D rooms live and in person</p>
    </div>

    <div class="programme programme--showroom">
      <span class="programme__label">OUR SHOWROOM</span>
      <p class="programme__items">A reflection of individuality + creativity</p>
    </div>

    <svg class="rule rule--lower" viewBox="0 0 434 12" aria-hidden="true">
      <line x1="6" y1="6" x2="428" y2="6" stroke="#e04b24" stroke-width="1.4"/>
      <path d="M2 0 L6 6 L2 12 Z M432 0 L428 6 L432 12 Z" fill="#e04b24"/>
      <circle cx="217" cy="6" r="1.6" fill="#e04b24"/>
    </svg>

    <p class="venue">1010 Vienna, Lindenring 22 / at Ahornplatz<br>on the ground floor and on the 1st floor</p>
  </section>
</main>
</body>
</html>
```